Biz Card for Harrowfield Property Partners - HWPP

Harrowfield Property Partners is a commercial real estate acquisitions firm. We buy commercial property and need to raise capital from investors for each deal we buy. The vibe needs to be: give us your money, we will multiply it.
Our website: www.hrwpp-example.com
Competitors are: https://velmarholdings-example.com/, https://tribanquepartners-example.com/, http://www.ostrellecapital-example.com/
Target Market(s)
High Net Worth Individuals, Bankers, Insurance Companies, Commercial Real Estate Brokers.
Industry/Entity Type
Investment Banking
Contact Information for Business Card
Name, Title, Addess, Cell#, Office#, email, website
Requirements
Must have
- use one of our logos. See website for look and feel: www.hrwpp-example.com
Nice to have
- see website: www.hrwpp-example.com

```html
<!DOCTYPE html>
<html lang="en">
<head>
<meta charset="utf-8">
<title>Harrowfield Property Partners – Business Cards</title>
<link rel="stylesheet" href="https://fonts.googleapis.com/css2?family=Lato:wght@400&family=Montserrat:ital,wght@0,500;0,700;1,500&display=swap">
<style>
  :root {
    --backdrop: #80b1dd;
    --navy: #132543;
    --navy-deep: #0f1a36;
    --mark-light: #8a93b4;
    --paper: #ffffff;
    --ink: #111a2c;
    --muted: #6b6f78;
    --rule: #2a2f3a;
  }
  * { margin: 0; padding: 0; box-sizing: border-box; }
  html, body { width: 1200px; height: 1200px; overflow: hidden; }
  body { background: var(--backdrop); position: relative; font-family: "Montserrat", sans-serif; }

  .card { position: absolute; box-shadow: 0 4px 10px rgba(20, 40, 80, 0.25); }

  /* Front */
  .card-front { left: 259px; top: 22px; width: 682px; height: 367px; background: var(--navy-deep); }
  .card-front .brand-dot {
    position: absolute; left: 83px; top: 112px; width: 144px; height: 144px;
    border-radius: 50%; background: var(--mark-light); opacity: 0.55;
  }
  .card-front .brand-name {
    position: absolute; left: 252px; top: 140px;
    font-family: "Lato", sans-serif; font-weight: 400; color: var(--mark-light);
  }
  .card-front .brand-name .line-main { display: block; font-size: 46px; letter-spacing: 5px; line-height: 1; }
  .card-front .brand-name .line-sub { display: block; font-size: 20px; letter-spacing: 6px; margin-top: 16px; }

  /* Back */
  .card-back { left: 261px; width: 688px; height: 370px; background: var(--paper); }
  .card-back.first { top: 413px; }
  .card-back.second { top: 806px; }

  .card-back .brand-dot {
    position: absolute; left: 131px; top: 105px; width: 92px; height: 92px;
    border-radius: 50%; background: var(--navy);
  }
  .card-back .brand-name {
    position: absolute; left: 20px; width: 314px; top: 212px; text-align: center;
    font-family: "Lato", sans-serif; font-weight: 400; color: var(--navy);
  }
  .card-back .brand-name .line-main { display: block; font-size: 28px; letter-spacing: 3px; line-height: 1; }
  .card-back .brand-name .line-sub { display: block; font-size: 12px; letter-spacing: 3.5px; margin-top: 10px; }

  .card-back .divider { position: absolute; left: 343px; top: 55px; width: 1px; height: 258px; background: var(--rule); }

  .person { position: absolute; left: 408px; top: 80px; }
  .person .name { font-size: 23px; font-weight: 700; color: var(--navy); line-height: 1.2; }
  .person .role { font-size: 12px; font-style: italic; font-weight: 500; color: var(--muted); margin-top: 2px; margin-left: 2px; }

  .contact-list { position: absolute; left: 403px; top: 147px; list-style: none; }
  .contact-list li { position: absolute; left: 0; display: flex; align-items: center; width: 280px; }
  .contact-list .icon { width: 28px; height: 28px; border-radius: 50%; background: var(--navy); flex: none; display: flex; align-items: center; justify-content: center; }
  .contact-list .icon svg { width: 13px; height: 13px; fill: var(--paper); }
  .contact-list .text { margin-left: 13px; font-size: 12px; font-weight: 500; color: var(--ink); line-height: 1.45; }
  .contact-list .address { top: 0; }
  .contact-list .email { top: 42px; }
  .contact-list .phone { top: 76px; }
  .contact-list .web { top: 108px; }
</style>
</head>
<body>

<section class="card card-front">
  <div class="brand-dot"></div>
  <div class="brand-name"><span class="line-main">HARROWFIELD</span><span class="line-sub">PROPERTY PARTNERS</span></div>
</section>

<section class="card card-back first">
  <div class="brand-dot"></div>
  <div class="brand-name"><span class="line-main">HARROWFIELD</span><span class="line-sub">PROPERTY PARTNERS</span></div>
  <div class="divider"></div>
  <div class="person">
    <h1 class="name">Daniel Ostrander</h1>
    <p class="role">Manager</p>
  </div>
  <ul class="contact-list">
    <li class="address"><span class="icon"><svg viewBox="0 0 24 24"><path d="M12 2a7 7 0 0 0-7 7c0 5 7 13 7 13s7-8 7-13a7 7 0 0 0-7-7zm0 9.5A2.5 2.5 0 1 1 12 6.5a2.5 2.5 0 0 1 0 5z"/></svg></span><span class="text">418 Larkspur Ave, Suite 900<br>Weston Bay, FL 33291</span></li>
    <li class="email"><span class="icon"><svg viewBox="0 0 24 24"><path d="M3 5h18v2l-9 6-9-6z M3 9l9 6 9-6v10H3z"/></svg></span><span class="text">dostrander@hrwpp-example.com</span></li>
    <li class="phone"><span class="icon"><svg viewBox="0 0 24 24"><path d="M6.6 10.8a15 15 0 0 0 6.6 6.6l2.2-2.2c.3-.3.7-.4 1-.2 1.1.4 2.3.6 3.6.6.6 0 1 .4 1 1V20c0 .6-.4 1-1 1A17 17 0 0 1 3 4c0-.6.4-1 1-1h3.5c.6 0 1 .4 1 1 0 1.3.2 2.5.6 3.6.1.3 0 .7-.2 1z"/></svg></span><span class="text">(555) 214-0386</span></li>
    <li class="web"><span class="icon"><svg viewBox="0 0 24 24"><path d="M12 2a10 10 0 1 0 0 20 10 10 0 0 0 0-20zm7.9 9h-3.4a15 15 0 0 0-1.3-6A8 8 0 0 1 19.9 11zM12 4c.9 1.2 2 3.6 2.4 7H9.6C10 7.6 11.1 5.2 12 4zM8.8 5a15 15 0 0 0-1.3 6H4.1A8 8 0 0 1 8.8 5zM4.1 13h3.4a15 15 0 0 0 1.3 6A8 8 0 0 1 4.1 13zM12 20c-.9-1.2-2-3.6-2.4-7h4.8c-.4 3.4-1.5 5.8-2.4 7zm3.2-1a15 15 0 0 0 1.3-6h3.4a8 8 0 0 1-4.7 6z"/></svg></span><span class="text">https://hrwpp-example.com/</span></li>
  </ul>
</section>

<section class="card card-back second">
  <div class="brand-dot"></div>
  <div class="brand-name"><span class="line-main">HARROWFIELD</span><span class="line-sub">PROPERTY PARTNERS</span></div>
  <div class="divider"></div>
  <div class="person">
    <h1 class="name">Miguel A. Ferrant</h1>
    <p class="role">Manager</p>
  </div>
  <ul class="contact-list">
    <li class="address"><span class="icon"><svg viewBox="0 0 24 24"><path d="M12 2a7 7 0 0 0-7 7c0 5 7 13 7 13s7-8 7-13a7 7 0 0 0-7-7zm0 9.5A2.5 2.5 0 1 1 12 6.5a2.5 2.5 0 0 1 0 5z"/></svg></span><span class="text">418 Larkspur Ave, Suite 900<br>Weston Bay, FL 33291</span></li>
    <li class="email"><span class="icon"><svg viewBox="0 0 24 24"><path d="M3 5h18v2l-9 6-9-6z M3 9l9 6 9-6v10H3z"/></svg></span><span class="text">mferrant@hrwpp-example.com</span></li>
    <li class="phone"><span class="icon"><svg viewBox="0 0 24 24"><path d="M6.6 10.8a15 15 0 0 0 6.6 6.6l2.2-2.2c.3-.3.7-.4 1-.2 1.1.4 2.3.6 3.6.6.6 0 1 .4 1 1V20c0 .6-.4 1-1 1A17 17 0 0 1 3 4c0-.6.4-1 1-1h3.5c.6 0 1 .4 1 1 0 1.3.2 2.5.6 3.6.1.3 0 .7-.2 1z"/></svg></span><span class="text">(555) 214-0386</span></li>
    <li class="web"><span class="icon"><svg viewBox="0 0 24 24"><path d="M12 2a10 10 0 1 0 0 20 10 10 0 0 0 0-20zm7.9 9h-3.4a15 15 0 0 0-1.3-6A8 8 0 0 1 19.9 11zM12 4c.9 1.2 2 3.6 2.4 7H9.6C10 7.6 11.1 5.2 12 4zM8.8 5a15 15 0 0 0-1.3 6H4.1A8 8 0 0 1 8.8 5zM4.1 13h3.4a15 15 0 0 0 1.3 6A8 8 0 0 1 4.1 13zM12 20c-.9-1.2-2-3.6-2.4-7h4.8c-.4 3.4-1.5 5.8-2.4 7zm3.2-1a15 15 0 0 0 1.3-6h3.4a8 8 0 0 1-4.7 6z"/></svg></span><span class="text">https://hrwpp-example.com/</span></li>
  </ul>
</section>

</body>
</html>
```